FOOD PACKAGING DESIGN FOR TRIVELLO KITCHENS - BRIEF UPDATED..

Hello Everyone

After discussions with Makerfold and the amount of work on this project, we have decided to split this project into phase 1 and phase 2 to make it more fair.

The allocated design budget is for Phase 1 only but we have included phase 2 below so you see the long term vision on this.

Phase 1 are products which we would like immediate designs on, once a winner is selected we will agree a fee with the designer via makerfold and design phase 2 products too.

This will ensure a reasonable number of designs for each phase.

After the successful design of a logo on makerfold, this is a packaging design project for Trivello Kitchens‎.

Initially this is not guaranteed as on a couple of occasions in the past we have been disappointed with the response but as soon as we receive a couple of designs that we believe we can take live, IMMEDIATELY WE WILL PAYMENT GUARANTEE THIS PROJECT, WITHOUT ANY HESITATION AND THIS IS NOT OUR FIRST PROJECT ON MAKERFOLD, PAYMENT HAS ALREADY BEEN MADE TO MAKERFOLD, IT IS JUST A MATTER OF RECEIVING SOME GOOD DESIGNS NOW AND WE’LL GUARANTEE IT.

This will be a big design project so we only want designers that can work with us on this long term.

We are a frozen food manufacturer and wholesaler and we are now looking to launch a retail brand under the name Trivello Kitchens, you can find more information about our company and what we sell by visiting our main website www.glaciermarten.example .

All the packaging we design will be for frozen food packaging.

The packaging will be frozen food bags and also folding carton boxes.

PHASE 1 BAGS:

Samosas:

1. 10, 20 and 50 Pack Meat ‎Samosas – One design but 3 pack sizes for all.
2. 10, 20 and 50 Pack Chicken Samosas
3. 10, 20 and 50 Pack Vegetable Samosas
4. 10, 20 and 50 Pack Chicken Tikka Samosas

Spring Rolls:

5. 10, 20 and 50 Pack Meat Spring Rolls – Again, one design but 3 pack sizes.
6. 10, 20 and 50 Pack Chicken Spring Rolls
7. 10, 20 and 50 Pack Vegetable Spring Rolls
8. 10, 20 and 50 Pack Chicken Tikka Spring Rolls

Seekh Kebabs:

9. 10 and 20 Pack Meat Seekh Kebabs – Ready Cooked (small writing not heading).
10. 10 and 20 Pack Chicken Seekh Kebabs – Ready Cooked (small writing not heading).

Chapli Kebabs:

11. Meat Chapli Kebabs, 8 Pack (500g) – Ready Cooked (small writing not heading).
12. Chicken Chapli Kebabs, 8 Pack (500g) – Ready Cooked (small writing not heading).

Doners and Shawarma Kebabs:

13. Cooked, Sliced, Traditional Doner Kebab – 1kg

Sausages:

14. 10 and 20 Pack Lamb Sausages
15. 10 and 20 Pack Beef Sausages
16. 10 and 20 Pack Chicken Sausages

Coated Chicken Range:

17. 750g and 1kg Battered Chicken Nuggets
18. 750g and 1kg‎ Breaded Chicken Nuggets

19. 750g and 1kg Battered Chicken Pops
20. 750g and 1kg‎ Breaded Chicken Pops

21. 750g and 1kg Battered Chicken Goujon Strips

22. 750g and 1kg‎ Breaded Chicken Goujon Strips

23. 10 Battered Chicken Burgers – Approx 850g
24. 10 Breaded Chicken Burgers – Approx 850g
25. 10 Southern Fried Chicken Burgers – Approx 850g

26. 1kg Battered Chicken Wings
27. 1kg Breaded Chicken Wings

BOXES – FOLDING CARTONS – PHASE 1:

Boxes will be as follows:

Burgers:

1. 8 Pack - Beef Burgers
2. 8 Pack - Chicken Burgers
3. 8 Pack - Lamb Burgers

PHASE 2 BAGS:

Shami Kebabs:

1. Meat Shami Kebabs, 8 Pack (500g) – Ready Cooked (small writing not heading).
2. Chicken Shami Kebabs‎, 8 Pack (500g) – Ready Cooked (small writing not heading).

1. Cooked, Sliced, Plain Chicken Shawarma – 1 kg
2. Cooked, Sliced, Tandoori Chicken Shawarma – 1 kg
3. Cooked, Sliced, Chicken Tikka Shawarma – 1 kg

Chicken Wings:

1. 1kg Hot & Spicy Chicken Wings
2. 1kg BBQ Chicken Wings
3. 1kg Peri Peri Chicken Wings
4. 1kg Tandoori Chicken Wings

At this stage we are looking for the design ideas and we’ll confirm the exact bag size when we select the final winner, here are some size guidelines:

• 10 Pack Bag Size – Length 23cm x Width 23cm
• 20 Pack Bag Size – Length 29cm x Width 24cm
• 50 Pack Bag Size – Length 34cm x Width 31cm
• 500g Bag Size – Length 27cm x Width 24cm
• 750g Bag Size – Length 29cm x Width 24cm
• 1kg Bag Size – Length 31cm x Width 27cm

BOXES – FOLDING CARTONS – PHASE 2:

Boxes will be as follows:

Seekh Kebabs:

1. 10 Pack and 20 Pack Lamb Seekh Kebabs – Ready Cooked (small writing not heading).

2. 10 Pack and 20 Pack Chicken Seekh Kebabs – Ready Cooked (small writing not heading).

Sausages:

3. 10 Pack Lamb Sausages
4. 10 Pack Beef Sausages
5. 10 Pack Chicken Sausages

6. 10 Pack Lamb Sausage Rolls
7. 10 Pack Beef Sausage Rolls
8. 10 Pack Chicken Sausage Rolls

Pies:

9. Chicken & Mushroom Pie – 12cm Length x 12cm Width x 4cm Depth
10. Chicken Tikka Pie – 12cm Length x 12cm Width x 5cm Depth
11. Steak & Kidney Pie – 12cm Length x 12cm Width x 4cm Depth
12. Meat & Onion Pie – 12cm Length x 12cm Width x 4cm Depth
13. Meat & Potato Pie – 12cm Length x 12cm Width x 5.5cm Depth

Pasties:

14. Chicken Tikka Pasty – 12cm Length x 12cm Width x 5cm Depth
15. Chicken & Sweetcorn Pasty – 12cm Length x 12cm Width x 5cm Depth
16. Keema Pasty – 12cm Length x 12cm Width x 5cm Depth

Ready Meals:

16cm Length x 16cm Width x 5cm

17. Lasagne
18. Chicken Curry & Rice
19. Chicken Tikka Masala & Rice
20. Butter Chicken & Rice
21. Chicken Jalfrezi & Rice
22. Chicken Saag & Rice
23. Lamb Curry & Rice
24. Lamb Rogan Josh & Rice
25. Daal Makhni & Rice
26. Mattar Paneer & Rice

Box Sizes:

• 10 Pack Box – Length 12cm x Width 25cm x Depth 5cm
• 20 Pack Box – To be Confirmed.
• Ready Meals - 16cm Length x 16cm Width x 5cm

The packaging that is designed must be clean and crisp with a classy premium feel to it, see the attached examples or email us for more ideas of what we like.

18. https://www.pinboardly.example/pin/100000000000000001/
19. https://www.pinboardly.example/pin/1000000000000002/
20. https://www.pinboardly.example/pin/100000000000000003/
21. https://www.pinboardly.example/pin/10000000000000004/
22. https://www.pinboardly.example/pin/1000000000000005/
23. https://www.pinboardly.example/pin/100000000000000006/
24. https://www.pinboardly.example/pin/100000000000000007/
25. https://www.pinboardly.example/pin/100000000000000008/
26. https://vellumgreens.example/products/
27. http://www.boxcritic.example/blog/2017/4/4/norvik-creamery-updated-packaging-now-features-a-mosaic-of-taste
28. https://www.pinboardly.example/pin/100000000000000009/
29. https://www.pinboardly.example/pin/100000000000000010/
30. https://www.folioweave.example/gallery/1000011/TONIC-WRAPPER
31. https://www.pinboardly.example/pin/100000000000000012/
32. https://www.pinboardly.example/pin/100000000000000013/
33. https://www.pinboardly.example/pin/100000000000000014/
34. https://www.pinboardly.example/pin/100000000000000015/

Our Competitors:

To help the designers, we have enclosed some links below of what our competitors are doing and how their packaging is designed, please note we don’t want anyone to copy their designs, ideas or styles, we are looking for something original but these links are given to help you so you can see what others are doing in our industry:

• http://dorvantfoods.example/products/ - Samosas, Spring Rolls, Kebabs etc, Bags
• http://www.plx-eats.example/ - Burgers, Sausages, Kebabs etc, folding cartons.
• http://tastewharf.example/assets/product-catalogue-2016.pdf - all foods
• https://cobaltlane.example/frozen-meals/ - ready meals

The packaging will have the following details on it:

1. Images of products for example sausages, burgers, chicken nuggets etc.

2. Quantity per pack - Front

3. Weight per pack – Front or Back.

4. Bar code – Back – to be provided for each item once winner is selected.

5. Halal logo at front‎.

6. Ingredients - Back

7. Possibly multilingual ingredients - Back, English, French, German etc.

8. Cooking instructions – Back.

9. Nutritional information table - Back.

10. Factory health mark of where the product is manufactured - Back

11. Contact details stating, "Trivellos is a Glacier Marten brand", followed by contact details, Tel: +44 (0) 800 555 0147, hello@glaciermarten.example, www.glaciermarten.example, www.trivellokitchens.example

We have attached some images of samosas, spring rolls, burgers, kebabs, pies and pasties etc to help with the design but you don’t have to use these images you can select your own at the initial stage, if we don’t like the image, we will provide these or we’ll select from picvault, frame depot etc.

The winning Trivello Kitchens Logo from Makerfold has been attached.

Glacier Marten (parent company logo) has also been attached so it can be used on the back of each packaging.

This will be an ongoing project where there will be regular work for the designer that is selected as the brand grows and we add more products to the brand.

Initially we are just looking for ideas on the packaging design but once finalised we would need it adjusted to the correct print size and resolution.

Thank you and we look forward to receiving your packaging ideas.

Glacier Marten

Food and drink industry, general public, halal market, Muslim customer base.

• Please read brief.
• Please read brief.

```html
<!DOCTYPE html>
<html lang="en">
<head>
<meta charset="utf-8">
<title>Trivello Kitchens Samosas Range</title>
<link rel="stylesheet" href="https://fonts.googleapis.com/css2?family=Tinos&family=Roboto+Condensed:wght@400;500&display=swap">
<style>
  :root {
    --board-grey: #8e979c;
    --board-light: #f2f3f4;
    --white: #ffffff;
    --meat: #a81d20;
    --meat-dark: #7e1214;
    --chicken: #f3923f;
    --chicken-dark: #d8732a;
    --tikka: #f26843;
    --tikka-dark: #d64a2a;
    --veg: #3fa844;
    --veg-dark: #2a8a33;
    --photo-light: #e9cfa8;
    --photo-dark: #c99a66;
    --halal: #1f6b3a;
    --frost: #a9cbe3;
    --frost-text: #7fa9c8;
    --ink: #222222;
    --brand-ink: #2a3f8f;
  }
  * { box-sizing: border-box; margin: 0; padding: 0; }
  html, body { width: 1200px; height: 923px; overflow: hidden; }
  body {
    position: relative;
    background: radial-gradient(ellipse at center, var(--board-light) 30%, var(--board-grey) 100%);
    font-family: "Tinos", "Times New Roman", serif;
  }
  .board {
    position: absolute;
    left: 5px; top: 135px;
    width: 1191px; height: 652px;
    background: var(--white);
  }
  .pack {
    position: absolute;
    width: 284px; height: 351px;
    background: var(--white);
    box-shadow: 0 0 18px rgba(0,0,0,0.22);
  }
  .pack--meat { left: 26px; top: 157px; --accent: var(--meat); --accent-dark: var(--meat-dark); }
  .pack--chicken { left: 315px; top: 244px; --accent: var(--chicken); --accent-dark: var(--chicken-dark); }
  .pack--tikka { left: 603px; top: 328px; --accent: var(--tikka); --accent-dark: var(--tikka-dark); }
  .pack--veg { left: 891px; top: 415px; --accent: var(--veg); --accent-dark: var(--veg-dark); }

  .band { position: absolute; left: 0; width: 100%; height: 31px; }
  .band--top { top: 0; background: linear-gradient(to bottom, var(--accent-dark), var(--accent)); }
  .band--bottom { bottom: 0; background: linear-gradient(to bottom, var(--accent), var(--accent-dark)); }

  .brand {
    position: absolute; left: 12px; top: 44px;
    display: flex; align-items: center; gap: 4px;
    font-size: 11px; color: var(--brand-ink);
  }
  .brand__dot { width: 9px; height: 9px; border-radius: 50%; background: var(--brand-ink); }

  .title {
    position: absolute; left: 67px; top: 134px;
    color: var(--accent); line-height: 1; font-weight: 400;
  }
  .title__flavour { display: block; font-size: 21px; }
  .title__product { display: block; font-size: 28px; letter-spacing: 2.5px; margin-top: 2px; }

  .count {
    position: absolute; left: 0; top: 216px;
    width: 70px; height: 33px;
    background: var(--accent);
    border-radius: 0 6px 6px 0;
    display: flex; align-items: center; justify-content: center; gap: 1px;
    color: var(--white);
    font-family: "Roboto Condensed", "Arial Narrow", sans-serif;
  }
  .count__num { font-size: 31px; letter-spacing: -2px; line-height: 1; }
  .count__label { font-size: 10px; writing-mode: vertical-rl; transform: rotate(180deg); letter-spacing: 0.5px; }

  .product-photo {
    position: absolute; left: 104px; top: 222px;
    width: 106px; height: 94px;
    border-radius: 4px;
    background: linear-gradient(to bottom, var(--photo-light), var(--photo-dark));
  }

  .halal-mark {
    position: absolute; left: 13px; top: 276px;
    width: 36px; height: 36px; border-radius: 50%;
    background: var(--halal); border: 2px solid var(--white);
    box-shadow: 0 0 0 1px var(--halal);
  }
  .weight {
    position: absolute; left: 53px; top: 289px;
    font-family: "Roboto Condensed", "Arial Narrow", sans-serif;
    font-size: 14px; color: var(--ink);
  }
  .keep-frozen { position: absolute; left: 219px; top: 268px; width: 46px; height: 48px; }
</style>
</head>
<body>
  <div class="board"></div>

  <section class="pack pack--meat">
    <div class="band band--top"></div>
    <div class="brand"><span class="brand__dot"></span>Trivello Kitchens</div>
    <h2 class="title"><span class="title__flavour">Meat</span><span class="title__product">SAMOSAS</span></h2>
    <div class="count"><span class="count__num">10</span><span class="count__label">PACK</span></div>
    <div class="product-photo" role="img" aria-label="Photo of a halved golden samosa showing spiced mince and pea filling"></div>
    <div class="halal-mark"></div>
    <div class="weight">325g</div>
    <svg class="keep-frozen" viewBox="0 0 46 48" aria-label="Keep frozen">
      <g stroke="var(--frost)" stroke-width="2" stroke-linecap="round">
        <line x1="23" y1="3" x2="23" y2="31"/><line x1="11" y1="10" x2="35" y2="24"/><line x1="35" y1="10" x2="11" y2="24"/>
      </g>
      <text x="23" y="40" text-anchor="middle" font-family="Roboto Condensed, sans-serif" font-size="8" fill="var(--frost-text)">KEEP</text>
      <text x="23" y="47" text-anchor="middle" font-family="Roboto Condensed, sans-serif" font-size="8" fill="var(--frost-text)">FROZEN</text>
    </svg>
    <div class="band band--bottom"></div>
  </section>

  <section class="pack pack--chicken">
    <div class="band band--top"></div>
    <div class="brand"><span class="brand__dot"></span>Trivello Kitchens</div>
    <h2 class="title"><span class="title__flavour">Chicken</span><span class="title__product">SAMOSAS</span></h2>
    <div class="count"><span class="count__num">10</span><span class="count__label">PACK</span></div>
    <div class="product-photo" role="img" aria-label="Photo of a halved golden samosa showing spiced chicken and pea filling"></div>
    <div class="halal-mark"></div>
    <div class="weight">325g</div>
    <svg class="keep-frozen" viewBox="0 0 46 48" aria-label="Keep frozen">
      <g stroke="var(--frost)" stroke-width="2" stroke-linecap="round">
        <line x1="23" y1="3" x2="23" y2="31"/><line x1="11" y1="10" x2="35" y2="24"/><line x1="35" y1="10" x2="11" y2="24"/>
      </g>
      <text x="23" y="40" text-anchor="middle" font-family="Roboto Condensed, sans-serif" font-size="8" fill="var(--frost-text)">KEEP</text>
      <text x="23" y="47" text-anchor="middle" font-family="Roboto Condensed, sans-serif" font-size="8" fill="var(--frost-text)">FROZEN</text>
    </svg>
    <div class="band band--bottom"></div>
  </section>

  <section class="pack pack--tikka">
    <div class="band band--top"></div>
    <div class="brand"><span class="brand__dot"></span>Trivello Kitchens</div>
    <h2 class="title"><span class="title__flavour">Chicken Tikka</span><span class="title__product">SAMOSAS</span></h2>
    <div class="count"><span class="count__num">10</span><span class="count__label">PACK</span></div>
    <div class="product-photo" role="img" aria-label="Photo of a halved golden samosa showing chicken tikka filling"></div>
    <div class="halal-mark"></div>
    <div class="weight">325g</div>
    <svg class="keep-frozen" viewBox="0 0 46 48" aria-label="Keep frozen">
      <g stroke="var(--frost)" stroke-width="2" stroke-linecap="round">
        <line x1="23" y1="3" x2="23" y2="31"/><line x1="11" y1="10" x2="35" y2="24"/><line x1="35" y1="10" x2="11" y2="24"/>
      </g>
      <text x="23" y="40" text-anchor="middle" font-family="Roboto Condensed, sans-serif" font-size="8" fill="var(--frost-text)">KEEP</text>
      <text x="23" y="47" text-anchor="middle" font-family="Roboto Condensed, sans-serif" font-size="8" fill="var(--frost-text)">FROZEN</text>
    </svg>
    <div class="band band--bottom"></div>
  </section>

  <section class="pack pack--veg">
    <div class="band band--top"></div>
    <div class="brand"><span class="brand__dot"></span>Trivello Kitchens</div>
    <h2 class="title"><span class="title__flavour">Vegetable</span><span class="title__product">SAMOSAS</span></h2>
    <div class="count"><span class="count__num">10</span><span class="count__label">PACK</span></div>
    <div class="product-photo" role="img" aria-label="Photo of a halved golden samosa showing spiced vegetable filling"></div>
    <div class="halal-mark"></div>
    <div class="weight">325g</div>
    <svg class="keep-frozen" viewBox="0 0 46 48" aria-label="Keep frozen">
      <g stroke="var(--frost)" stroke-width="2" stroke-linecap="round">
        <line x1="23" y1="3" x2="23" y2="31"/><line x1="11" y1="10" x2="35" y2="24"/><line x1="35" y1="10" x2="11" y2="24"/>
      </g>
      <text x="23" y="40" text-anchor="middle" font-family="Roboto Condensed, sans-serif" font-size="8" fill="var(--frost-text)">KEEP</text>
      <text x="23" y="47" text-anchor="middle" font-family="Roboto Condensed, sans-serif" font-size="8" fill="var(--frost-text)">FROZEN</text>
    </svg>
    <div class="band band--bottom"></div>
  </section>
</body>
</html>
```